Business card for auto dealership

Looking for a clean modern design.
Would like attached logo incorporated

Industry/Entity Type

Car dealership

Contact Information for Business Card

Name, website, phone, cell, fax, email

```html
<!DOCTYPE html>
<html lang="en">
<head>
<meta charset="utf-8">
<title>Halvorsen Truck &amp; Auto Sales – Business Card</title>
<link rel="stylesheet" href="https://fonts.googleapis.com/css2?family=Red+Hat+Display:wght@700;900&display=swap">
<style>
  :root {
    --page-bg: #eef0f3;
    --card-bg: #ffffff;
    --brand-red: #ed1c24;
    --ink-navy: #262466;
    --ink-black: #111111;
    --font-main: "Red Hat Display", "Helvetica Neue", Arial, sans-serif;
  }
  * { box-sizing: border-box; margin: 0; padding: 0; }
  html, body {
    width: 1200px; height: 1000px; overflow: hidden;
    background: var(--page-bg);
    font-family: var(--font-main);
  }
  .canvas { position: relative; width: 1200px; height: 1000px; }

  .card {
    position: absolute;
    background: var(--card-bg);
    overflow: hidden;
  }
  .card-front { left: 227px; top: 35px; width: 740px; height: 412px; }
  .card-back  { left: 219px; top: 482px; width: 748px; height: 415px; }

  .card-swoosh { position: absolute; inset: 0; width: 100%; height: 100%; }
  .card-swoosh path { fill: var(--brand-red); }

  .wordmark {
    position: absolute;
    color: var(--ink-black);
    font-weight: 900;
    text-align: right;
    line-height: 1;
  }
  .wordmark-name { display: block; letter-spacing: -0.02em; }
  .wordmark-tag  { display: block; letter-spacing: 0.02em; }

  .card-front .wordmark { left: 90px; top: 150px; width: 560px; }
  .card-front .wordmark-name { font-size: 104px; }
  .card-front .wordmark-tag  { font-size: 27px; margin-top: 16px; }

  .card-back .wordmark { left: 24px; top: 160px; width: 318px; }
  .card-back .wordmark-name { font-size: 60px; }
  .card-back .wordmark-tag  { font-size: 16px; margin-top: 8px; }

  .contact-list { list-style: none; position: absolute; left: 401px; top: 93px; }
  .contact-item {
    display: flex; align-items: center; gap: 14px;
    height: 36px; margin-bottom: 9px;
    color: var(--ink-navy);
    font-size: 21px; font-weight: 700;
  }
  .contact-item.is-name { margin-bottom: 17px; }
  .contact-email { position: absolute; left: 206px; top: 328px; }

  .contact-icon { width: 36px; height: 36px; flex: none; }
  .contact-icon circle.badge { fill: var(--brand-red); }
  .contact-icon .glyph { fill: #fff; }
  .contact-icon .glyph-line { fill: none; stroke: #fff; stroke-width: 1.6; }
</style>
</head>
<body>
<main class="canvas">

  <section class="card card-front" aria-label="Card front">
    <svg class="card-swoosh" viewBox="0 0 740 412" preserveAspectRatio="none" aria-hidden="true">
      <path d="M0,235 Q190,370 425,412 L0,412 Z"/>
      <path d="M590,412 Q675,400 740,377 L740,412 Z"/>
    </svg>
    <div class="wordmark">
      <span class="wordmark-name">Halvorsen</span>
      <span class="wordmark-tag">TRUCK &amp; AUTO SALES</span>
    </div>
  </section>

  <section class="card card-back" aria-label="Card back">
    <svg class="card-swoosh" viewBox="0 0 748 415" preserveAspectRatio="none" aria-hidden="true">
      <path d="M0,0 H748 V13 Q430,-14 0,70 Z"/>
    </svg>
    <div class="wordmark">
      <span class="wordmark-name">Halvorsen</span>
      <span class="wordmark-tag">TRUCK &amp; AUTO SALES</span>
    </div>

    <ul class="contact-list">
      <li class="contact-item is-name">
        <svg class="contact-icon" viewBox="0 0 36 36" aria-hidden="true">
          <circle class="badge" cx="18" cy="18" r="17"/>
          <circle class="glyph" cx="18" cy="13.5" r="5"/>
          <path class="glyph" d="M9,27 Q9,19.5 18,19.5 Q27,19.5 27,27 Z"/>
        </svg>
        <span>Jordan Halvorsen</span>
      </li>
      <li class="contact-item">
        <svg class="contact-icon" viewBox="0 0 36 36" aria-hidden="true">
          <circle class="badge" cx="18" cy="18" r="17"/>
          <rect class="glyph-line" x="9" y="11.5" width="18" height="13"/>
          <path class="glyph-line" d="M9,11.5 L18,19 L27,11.5 M9,24.5 L15.5,17.5 M27,24.5 L20.5,17.5"/>
        </svg>
        <span>Halvorsenauto.com</span>
      </li>
      <li class="contact-item">
        <svg class="contact-icon" viewBox="0 0 36 36" aria-hidden="true">
          <circle class="badge" cx="18" cy="18" r="17"/>
          <path class="glyph" d="M8,14 Q8,9 18,9 Q28,9 28,14 L28,16 L23,16 L23,13.5 L13,13.5 L13,16 L8,16 Z"/>
          <path class="glyph" d="M12,17 L24,17 L27,27 L9,27 Z"/>
        </svg>
        <span>555-014-2271</span>
      </li>
      <li class="contact-item">
        <svg class="contact-icon" viewBox="0 0 36 36" aria-hidden="true">
          <circle class="badge" cx="18" cy="18" r="17"/>
          <rect class="glyph" x="11" y="8" width="14" height="20" rx="1.5"/>
          <rect x="13.5" y="10.5" width="9" height="4" fill="#ed1c24"/>
          <path d="M13.5,17h2v2h-2zM17,17h2v2h-2zM20.5,17h2v2h-2zM13.5,20.5h2v2h-2zM17,20.5h2v2h-2zM20.5,20.5h2v2h-2z" fill="#ed1c24"/>
        </svg>
        <span>555-019-3386</span>
      </li>
      <li class="contact-item">
        <svg class="contact-icon" viewBox="0 0 36 36" aria-hidden="true">
          <circle class="badge" cx="18" cy="18" r="17"/>
          <rect class="glyph" x="12" y="7.5" width="12" height="21" rx="2"/>
          <rect x="13.8" y="10.5" width="8.4" height="13.5" fill="#ed1c24"/>
        </svg>
        <span>555-017-4402</span>
      </li>
    </ul>

    <div class="contact-item contact-email">
      <svg class="contact-icon" viewBox="0 0 36 36" aria-hidden="true">
        <circle class="badge" cx="18" cy="18" r="17"/>
        <circle class="glyph-line" cx="18" cy="18" r="9.5"/>
        <ellipse class="glyph-line" cx="18" cy="18" rx="4.2" ry="9.5"/>
        <path class="glyph-line" d="M8.5,18 H27.5 M10,13 H26 M10,23 H26 M18,8.5 V27.5"/>
      </svg>
      <span>jordan@halvorsenauto.com</span>
    </div>
  </section>

</main>
</body>
</html>
```